teaching love. a joyful state of being.

adding value to ones circumstance through the teachings of neutralization. quote for back of card: "and then it happens... One day you wake up and you're in this place. You are in this place where everything is right. Your heart is calm. Your soul is lit. Your thoughts are positive. Your vision is clear. Your faith is stronger than ever. And you are at peace. At peace with where you have been. At peace with what you've been through. And at peace with where you're headed." -unknown

Target Market(s)

spiritual, awakening, inspiration, motivation, gratefulness, oneness, peace, positive mindset,

Contact Information for Business Card

front: one line message from quote

Logo Text

up to suggestions

Font styles to use
Serif
Sans Serif
Script

Colors

Designer to choose colors to be used in the design.

Requirements
Must have
• entire quote on one side of card
Nice to have
• simple, and to the point
Should not have
• elaborated designs

```html
<!DOCTYPE html>
<html lang="en">
<head>
<meta charset="utf-8">
<title>Business Card – Front and Back</title>
<link rel="stylesheet" href="https://fonts.googleapis.com/css2?family=Arvo:wght@400;700&family=Noto+Serif:wght@400;700&display=swap">
<style>
  :root {
    --backdrop: #e6e6e8;
    --card-black: #050505;
    --gold-deep: #c98a2a;
    --gold-mid: #e9bf63;
    --gold-light: #fbeec4;
    --gold-text: #d9a531;
    --ink: #111111;
    --pin: #555555;
    --shadow: rgba(0, 0, 0, 0.22);
  }
  * { box-sizing: border-box; margin: 0; padding: 0; }
  html, body {
    width: 1200px; height: 967px; overflow: hidden;
    background: var(--backdrop);
  }
  .canvas { position: relative; width: 1200px; height: 967px; }

  .card {
    position: absolute;
    width: 620px; height: 354px;
    border-radius: 30px;
    overflow: hidden;
    background: var(--card-black);
    box-shadow: 0 14px 30px var(--shadow);
  }
  .card--back { left: 510px; top: 90px; }
  .card--front { left: 80px; top: 510px; }

  /* Back: full quote */
  .quote {
    position: absolute; inset: 0;
    display: flex; flex-direction: column; justify-content: center; align-items: center;
    padding: 30px 40px;
    font-family: "Arvo", serif;
    font-weight: 700;
    font-size: 17.5px;
    line-height: 1.42;
    color: var(--gold-text);
    text-align: center;
    letter-spacing: 0.2px;
  }
  .quote__source { margin-top: 2px; }

  /* Front */
  .front-art { position: absolute; inset: 0; width: 100%; height: 100%; }

  .brand-name {
    position: absolute; left: 40px; top: 70px; width: 250px;
    font-family: "Noto Serif", serif;
    font-weight: 700;
    font-size: 46px;
    line-height: 1.15;
    color: var(--gold-text);
    text-align: center;
  }

  .contact-list {
    position: absolute; left: 26px; top: 262px;
    list-style: none;
    font-family: "Noto Serif", serif;
    color: var(--gold-text);
  }
  .contact-list li { display: flex; align-items: center; gap: 10px; height: 22px; }
  .contact-list svg { width: 18px; height: 18px; flex: none; }
  .contact-list .phone-number { font-family: "Arvo", serif; font-size: 21px; font-weight: 400; }
  .contact-list .email, .contact-list .web { font-size: 15px; }

  .identity {
    position: absolute; left: 372px; top: 80px; width: 236px;
    font-family: "Noto Serif", serif;
    color: var(--ink);
    text-align: center;
    font-size: 25px;
    line-height: 1.2;
  }

  .address {
    position: absolute; left: 414px; top: 238px;
    display: flex; align-items: flex-start; gap: 8px;
    font-family: "Noto Serif", serif;
    font-size: 13px;
    line-height: 1.2;
    color: var(--ink);
  }
  .address svg { width: 16px; height: 18px; margin-top: 4px; flex: none; }
</style>
</head>
<body>
<main class="canvas">

  <section class="card card--back" aria-label="Card back with quote">
    <blockquote class="quote">
      <p>"and then it happens... One day you<br>
      wake up and you're in this place. You<br>
      are in this place where everything is<br>
      right. Your heart is calm. Your soul is lit.<br>
      Your thoughts are positive. Your vision<br>
      is clear. Your faith is stronger than ever.<br>
      And you are at peace. At peace with<br>
      where you have been. At peace with what<br>
      you've been through. And at peace with<br>
      where you're headed."</p>
      <p class="quote__source">-unknown</p>
    </blockquote>
  </section>

  <section class="card card--front" aria-label="Card front">
    <svg class="front-art" viewBox="0 0 620 354" preserveAspectRatio="none" aria-hidden="true">
      <defs>
        <linearGradient id="gold-panel" x1="0" y1="0" x2="0" y2="1">
          <stop offset="0" stop-color="var(--gold-deep)"/>
          <stop offset="0.45" stop-color="var(--gold-light)"/>
          <stop offset="0.8" stop-color="var(--gold-mid)"/>
          <stop offset="1" stop-color="var(--gold-deep)"/>
        </linearGradient>
      </defs>
      <rect width="620" height="354" fill="var(--card-black)"/>
      <path d="M268 0 H620 V354 H418 C408 200 360 70 268 0 Z" fill="url(#gold-panel)"/>
    </svg>

    <div class="brand-name">Lumen<br>Peace</div>

    <ul class="contact-list">
      <li>
        <svg viewBox="0 0 18 18"><rect x="5" y="1.5" width="8" height="15" rx="1.5" fill="none" stroke="currentColor" stroke-width="1.4"/><line x1="8" y1="14" x2="10" y2="14" stroke="currentColor" stroke-width="1.4"/></svg>
        <span class="phone-number">+254 700 555 012</span>
      </li>
      <li>
        <svg viewBox="0 0 18 18"><rect x="2" y="4" width="14" height="10" rx="1" fill="none" stroke="currentColor" stroke-width="1.4"/><path d="M2 4 L9 10 L16 4" fill="none" stroke="currentColor" stroke-width="1.4"/></svg>
        <span class="email">amara.wanjiru@example.com</span>
      </li>
      <li>
        <svg viewBox="0 0 18 18"><circle cx="9" cy="9" r="7" fill="none" stroke="currentColor" stroke-width="1.4"/><ellipse cx="9" cy="9" rx="3" ry="7" fill="none" stroke="currentColor" stroke-width="1.2"/><line x1="2" y1="9" x2="16" y2="9" stroke="currentColor" stroke-width="1.2"/></svg>
        <span class="web">www.yourdomain.com</span>
      </li>
    </ul>

    <div class="identity">
      <p class="identity__name">Amara Wanjiru</p>
      <p class="identity__role">Manager</p>
    </div>

    <div class="address">
      <svg viewBox="0 0 16 18"><path d="M8 17 C4 12 2 9.5 2 7 A6 6 0 0 1 14 7 C14 9.5 12 12 8 17 Z" fill="none" stroke="var(--pin)" stroke-width="1.2"/><circle cx="8" cy="7" r="2" fill="none" stroke="var(--pin)" stroke-width="1.2"/></svg>
      <p>Street Name, Suit 1234<br>State, Zip Code, Country</p>
    </div>
  </section>

</main>
</body>
</html>
```